Business Card Designs

Looking to design a 3.5" x 2" standard business card for our employees.
The design needs to be sleek, simple, and modern. We would like our logo (attached) to be incorporated, but not in that colour, rather an outline of the logo in either gold or silver (whichever looks better).

Modern and Simple is what we are looking for, but be creative in incorporating the logo.

```html
<!DOCTYPE html>
<html lang="en">
<head>
<meta charset="utf-8">
<title>Harbourline Suites – Business Cards</title>
<link rel="stylesheet" href="https://fonts.googleapis.com/css2?family=Montserrat:wght@400;700&display=swap">
<style>
  :root {
    --page-bg: #8a8a8a;
    --card-bg: #231f20;
    --card-band: #2d2b2e;
    --card-top: #1b1819;
    --gold: #c9a94a;
    --gold-light: #e2c979;
    --text-light: #eeeeee;
    --teal: #5a9c95;
  }
  * { box-sizing: border-box; margin: 0; padding: 0; }
  html, body { width: 1200px; height: 900px; overflow: hidden; }
  body {
    background: var(--page-bg);
    font-family: "Montserrat", sans-serif;
    display: flex;
    align-items: center;
    justify-content: center;
    gap: 60px;
  }
  .card {
    position: relative;
    width: 350px;
    height: 600px;
    background: var(--card-bg);
    box-shadow: 0 18px 40px rgba(0,0,0,.45);
    overflow: hidden;
    display: flex;
    flex-direction: column;
    align-items: center;
  }
  .card__top-strip { position: absolute; top: 0; left: 0; right: 0; height: 22px; background: var(--card-top); }
  .card__band { position: absolute; top: 22px; left: 0; right: 0; height: 110px; background: var(--card-band); }
  .brand {
    position: relative;
    display: flex;
    align-items: center;
    gap: 10px;
    color: var(--gold);
    font-weight: 700;
    font-size: 19px;
    letter-spacing: 2px;
    text-transform: uppercase;
  }
  .brand__mark { width: 14px; height: 14px; background: var(--teal); flex: none; }
  .card--front .brand { margin-top: 430px; }
  .card--back .brand { margin-top: 150px; }
  .person { position: relative; margin-top: 120px; text-align: center; }
  .person__name { color: var(--gold); font-weight: 700; font-size: 18px; letter-spacing: 1px; text-transform: uppercase; }
  .person__role { color: var(--text-light); font-size: 14px; margin-top: 4px; }
  .icons { position: relative; display: flex; gap: 12px; margin-top: 50px; }
  .icons svg { width: 26px; height: 26px; }
  .contact { position: relative; margin-top: 20px; text-align: center; color: var(--text-light); font-size: 14px; line-height: 1.75; }
</style>
</head>
<body>
  <section class="card card--front">
    <div class="card__top-strip"></div>
    <div class="card__band"></div>
    <div class="brand"><span class="brand__mark"></span>Harbourline Suites</div>
  </section>

  <section class="card card--back">
    <div class="card__top-strip"></div>
    <div class="card__band"></div>
    <div class="brand"><span class="brand__mark"></span>Harbourline Suites</div>
    <div class="person">
      <p class="person__name">Daniel Reyes</p>
      <p class="person__role">Director</p>
    </div>
    <div class="icons">
      <svg viewBox="0 0 26 26" aria-label="Phone"><circle cx="13" cy="13" r="13" fill="var(--gold)"/><path d="M9 7l3 3-1.5 1.5a8 8 0 0 0 4 4L16 14l3 3-2 2C11 19 7 15 7 9z" fill="var(--card-bg)"/></svg>
      <svg viewBox="0 0 26 26" aria-label="Email"><circle cx="13" cy="13" r="13" fill="var(--gold)"/><rect x="7" y="9" width="12" height="8" fill="var(--card-bg)"/><path d="M7 9l6 5 6-5" stroke="var(--gold)" stroke-width="1.2" fill="none"/></svg>
      <svg viewBox="0 0 26 26" aria-label="Website"><circle cx="13" cy="13" r="13" fill="var(--gold)"/><circle cx="13" cy="13" r="6" fill="none" stroke="var(--card-bg)" stroke-width="1.5"/><path d="M7 13h12M13 7c-3 3-3 9 0 12M13 7c3 3 3 9 0 12" stroke="var(--card-bg)" stroke-width="1.2" fill="none"/></svg>
      <svg viewBox="0 0 26 26" aria-label="Address"><circle cx="13" cy="13" r="13" fill="var(--gold)"/><path d="M13 20s-5-5-5-9a5 5 0 0 1 10 0c0 4-5 9-5 9z" fill="var(--card-bg)"/><circle cx="13" cy="11" r="1.8" fill="var(--gold)"/></svg>
    </div>
    <div class="contact">
      <p>555-014-2280</p>
      <p>hello@harbourline.com</p>
      <p>www.harbourline.com</p>
      <p>42 Sample Street, Anytown 0000</p>
    </div>
  </section>
</body>
</html>
```